Tallow Crest Business Card

We need a business card designed for a a company called "Tallow Crest". We offer consulting, coaching and training to business leaders and coaches (across the world) using the latest findings in neuroscience, social and emotional intelligence and positive psychology. The final design should communicate the use of brain science to create sustainable relationships.

The card should be doublesided. The logo is attached and names and titles will be provided to the successful designer. Thank you.

Industry/Entity Type

Training

```html
<!DOCTYPE html>
<html lang="en">
<head>
<meta charset="utf-8">
<title>Tallow Crest Business Card</title>
<link rel="stylesheet" href="https://fonts.googleapis.com/css2?family=Roboto:wght@300;400;700&display=swap">
<style>
  :root {
    --page-bg: #d8d9da;
    --brand-blue: #1b8ec4;
    --brand-blue-deep: #1677ad;
    --brand-lime: #c6d936;
    --paper-white: #f7f8f8;
    --text-white: #ffffff;
  }
  * { box-sizing: border-box; margin: 0; padding: 0; }
  html, body { width: 1200px; height: 800px; overflow: hidden; }
  body {
    background: var(--page-bg);
    font-family: "Roboto", Arial, sans-serif;
    display: flex;
    align-items: center;
    justify-content: center;
    gap: 40px;
  }
  .card {
    position: relative;
    width: 540px;
    height: 309px;
    background: var(--brand-blue);
    overflow: hidden;
    box-shadow: 0 6px 18px rgba(0,0,0,0.18);
  }

  /* Front */
  .profile-panel {
    position: absolute;
    left: 0; top: 0;
    width: 300px; height: 100%;
    background: var(--paper-white);
  }
  .brand-name {
    position: absolute;
    left: 34px; top: 128px;
    font-weight: 700;
    font-size: 34px;
    color: var(--brand-blue-deep);
    display: flex;
    align-items: center;
    gap: 10px;
  }
  .brand-dot {
    width: 18px; height: 18px;
    border-radius: 50%;
    background: var(--brand-lime);
  }
  .holder {
    position: absolute;
    right: 26px; top: 24px;
    text-align: right;
    color: var(--text-white);
  }
  .holder-name { font-weight: 400; font-size: 19px; }
  .holder-title { font-weight: 300; font-size: 13px; margin-top: 2px; }
  .contact {
    position: absolute;
    right: 26px; bottom: 26px;
    text-align: right;
    font-weight: 300;
    font-size: 15px;
    line-height: 1.45;
    color: var(--text-white);
  }
  .contact .company { font-weight: 400; }
  .contact .address { color: var(--brand-lime); font-size: 13px; }
  .contact-line { display: flex; justify-content: flex-end; align-items: center; gap: 6px; }
  .contact-icon { width: 12px; height: 12px; flex: none; }

  /* Back */
  .back-site {
    position: absolute;
    right: 26px; top: 22px;
    color: var(--text-white);
    font-weight: 300;
    font-size: 13px;
  }
  .back-brand {
    position: absolute;
    left: 0; right: 0; top: 50%;
    transform: translateY(-50%);
    display: flex;
    justify-content: center;
    align-items: center;
    gap: 14px;
    font-weight: 700;
    font-size: 44px;
    color: var(--text-white);
  }
  .back-brand .brand-dot { width: 24px; height: 24px; }
</style>
</head>
<body>

  <section class="card card-front">
    <div class="profile-panel" role="img" aria-label="White head profile silhouette facing right"></div>
    <div class="brand-name"><span class="brand-dot"></span>Tallow Crest</div>

    <div class="holder">
      <div class="holder-name">Dana Whitfield</div>
      <div class="holder-title">Director</div>
    </div>

    <div class="contact">
      <div class="company">Tallow Crest LLC</div>
      <div class="address">804 Larkspur Lane</div>
      <div class="address">Fairbend, TX 77310</div>
      <div class="contact-line">1877-555-0142
        <svg class="contact-icon" viewBox="0 0 12 12"><rect x="3" y="0.5" width="6" height="11" rx="1.2" fill="none" stroke="#c6d936" stroke-width="1.2"/><circle cx="6" cy="9.6" r="0.8" fill="#c6d936"/></svg>
      </div>
      <div class="contact-line">info@tallowcrest.com
        <svg class="contact-icon" viewBox="0 0 12 12"><rect x="0.6" y="2.5" width="10.8" height="7" fill="none" stroke="#c6d936" stroke-width="1.2"/><path d="M0.6 2.5 6 6.8 11.4 2.5" fill="none" stroke="#c6d936" stroke-width="1.2"/></svg>
      </div>
      <div class="contact-line">www.tallowcrest.com
        <svg class="contact-icon" viewBox="0 0 12 12"><circle cx="6" cy="6" r="5.3" fill="none" stroke="#c6d936" stroke-width="1.2"/><path d="M0.7 6h10.6M6 0.7c2.4 2.8 2.4 7.8 0 10.6M6 0.7c-2.4 2.8-2.4 7.8 0 10.6" fill="none" stroke="#c6d936" stroke-width="1"/></svg>
      </div>
    </div>
  </section>

  <section class="card card-back">
    <div class="back-site">www.tallowcrest.com</div>
    <div class="back-brand"><span class="brand-dot"></span>Tallow Crest</div>
  </section>

</body>
</html>
```